Start-up Cleaning Business Needs Professional Business Cards

Marta's Butler Cleaning, LLC, is a start-up business based in the Northern Virginia suburbs of Washington, DC. MBC provides cleaning and housekeeping services for homes and offices. We have three core values:

1. We are personal. We value knowing and being known by our customers and each other. If you want nameless, faceless service, you should choose another provider. We put "personal" at the front of the list, because it is most important to us; the design we choose will convey this value.

2. Like a hotel concierge, we are professional in attitude, posture, communication and processes.

3. Like a hotel concierge, we solve problems with a can-do attitude and never make excuses.

Our uniforms are khaki pants with pink polo shirts.

Our logo is attached. There are other symbols, not represented in our logo, that may convey our values well, such as a top hat and bow tie, magnifying glass, desk bell, etc.

Please include fields for an individual's name and title, office phone number, mobile phone number, email address and website address (www.martasbutlercleaning.example).

Standard U.S. size: 2" x 3.5"
Updates

I should have mentioned that the purpose of all our advertising - business cards included - is to motivate potential customers to call or email to arrange a free in-home estimate.

```html
<!DOCTYPE html>
<html lang="en">
<head>
<meta charset="utf-8">
<title>Marta's Butler Cleaning — Business Card</title>
<link href="https://fonts.googleapis.com/css2?family=Questrial&display=swap" rel="stylesheet">
<style>
  :root {
    --page-bg: #e9e7e4;
    --card-bg: #ffffff;
    --card-tint: #fdf6f9;
    --pink: #e0297f;
    --pink-soft: #f6d9e6;
    --ink: #3a3a3a;
    --shadow: rgba(0, 0, 0, 0.18);
  }
  * { box-sizing: border-box; margin: 0; padding: 0; }
  html, body { width: 1200px; height: 1000px; overflow: hidden; }
  body {
    background: var(--page-bg);
    font-family: "Questrial", "Century Gothic", sans-serif;
    position: relative;
  }
  .card {
    position: absolute;
    left: 215px;
    width: 770px;
    height: 440px;
    background: linear-gradient(135deg, var(--card-bg) 0%, var(--card-tint) 100%);
    box-shadow: 0 6px 18px var(--shadow);
    overflow: hidden;
  }
  .card--contact { top: 40px; }
  .card--brand { top: 520px; }

  /* Contact side */
  .identity {
    position: absolute;
    right: 56px;
    top: 44px;
    text-align: right;
  }
  .identity__name {
    color: var(--pink);
    font-size: 30px;
    letter-spacing: 2px;
    text-transform: uppercase;
  }
  .identity__title {
    color: var(--ink);
    font-size: 22px;
    margin-top: 2px;
  }
  .contact-list {
    position: absolute;
    right: 56px;
    top: 150px;
    list-style: none;
  }
  .contact-list__item {
    display: flex;
    justify-content: flex-end;
    align-items: center;
    gap: 14px;
    color: var(--ink);
    font-size: 21px;
    height: 36px;
  }
  .contact-list__icon {
    width: 24px;
    height: 24px;
    flex: none;
  }
  .call-to-action {
    position: absolute;
    right: 56px;
    bottom: 36px;
    color: var(--pink);
    font-size: 23px;
    letter-spacing: 0.5px;
  }

  /* Brand side */
  .mascot-art {
    position: absolute;
    left: 300px;
    top: 30px;
    width: 260px;
    height: 250px;
    border-radius: 12px;
    background: linear-gradient(160deg, var(--pink-soft) 0%, #f3e4ea 60%, #ece2e4 100%);
  }
  .business-name {
    position: absolute;
    right: 60px;
    top: 330px;
    color: var(--ink);
    font-size: 34px;
    line-height: 1.2;
    white-space: nowrap;
  }
</style>
</head>
<body>

<section class="card card--contact" aria-label="Business card, contact side">
  <div class="identity">
    <p class="identity__name">Your Name</p>
    <p class="identity__title">Title</p>
  </div>

  <ul class="contact-list">
    <li class="contact-list__item">
      <span>123 456 7890</span>
      <svg class="contact-list__icon" viewBox="0 0 24 24" aria-hidden="true">
        <circle cx="12" cy="12" r="12" fill="var(--pink)"/>
        <path d="M8.2 6.5l2 2-1.2 1.4c.7 1.6 2 2.9 3.6 3.6l1.4-1.2 2 2-1.4 1.6c-3.6-.5-7-3.9-7.5-7.5z" fill="#fff"/>
      </svg>
    </li>
    <li class="contact-list__item">
      <span>123 456 7890</span>
      <svg class="contact-list__icon" viewBox="0 0 24 24" aria-hidden="true">
        <circle cx="12" cy="12" r="12" fill="var(--pink)"/>
        <rect x="8.5" y="5.5" width="7" height="13" rx="1.2" fill="#fff"/>
        <rect x="9.7" y="7.2" width="4.6" height="8" fill="var(--pink)"/>
      </svg>
    </li>
    <li class="contact-list__item">
      <span>yourname@mbcmail.example</span>
      <svg class="contact-list__icon" viewBox="0 0 24 24" aria-hidden="true">
        <circle cx="12" cy="12" r="12" fill="var(--pink)"/>
        <rect x="6" y="8" width="12" height="8.5" fill="#fff"/>
        <path d="M6 8l6 5 6-5" fill="none" stroke="var(--pink)" stroke-width="1.2"/>
      </svg>
    </li>
    <li class="contact-list__item">
      <span>www.martasbutlercleaning.example</span>
      <svg class="contact-list__icon" viewBox="0 0 24 24" aria-hidden="true">
        <circle cx="12" cy="12" r="12" fill="var(--pink)"/>
        <g fill="none" stroke="#fff" stroke-width="1.2">
          <circle cx="12" cy="12" r="6"/>
          <ellipse cx="12" cy="12" rx="2.6" ry="6"/>
          <path d="M6 12h12M7 9h10M7 15h10"/>
        </g>
      </svg>
    </li>
  </ul>

  <p class="call-to-action">Call or Email us to arrange a Free In-Home Estimate.</p>
</section>

<section class="card card--brand" aria-label="Business card, brand side">
  <div class="mascot-art" role="img" aria-label="Sketched illustration of a housekeeper in a pink uniform mopping the floor"></div>
  <p class="business-name">Marta's Butler Cleaning, LLC</p>
</section>

</body>
</html>
```